Polling website project

We need a website design for a polling website called votiqo.com. This will be a website where visitors can take and create polls for various topics along with view results. We want something really simple and "web 2.0." We are going to make a cell phone app that goes along with the website and we want the look and feel of the website to be very "app-like." Basically that means minimalistic design with a poll being the center of the page.
When someone comes to the site, we want them to see basically just a poll in the center of the screen and a toolbar at the top of the page with links to login fields/user profile, post a new poll, view friends list, a drop-down list of poll topics, and a search bar. We need about three pages mocked up: a home page/poll view page, a user control panel/profile page, a submit new poll page.
We also want our logo/header to have a "pulse" theme. The name votiqo is supposed to be a play on the word pulse, we'd like the logo to make that obvious, maybe the use of the EKG graph could work.
We also want a nice tab in the corner to sign up that is attractive and flashy, kind of like the feedback tab on the side of this website.
Target Market(s)
Teens and young adults, the chatterly crowd
Industry/Entity Type
Cell Phone
Look and feel
Each slider illustrates characteristics of the customer's brand and the style your logo design should communicate.

```html
<!DOCTYPE html>
<html lang="en">
<head>
<meta charset="utf-8">
<title>Votiqo – Home</title>
<link href="https://fonts.googleapis.com/css2?family=Arimo:wght@400;700&display=swap" rel="stylesheet">
<style>
:root{
  --sky-deep:#1b8fc0;
  --sky:#27a9dc;
  --sky-light:#4cc3ef;
  --white:#ffffff;
  --ink:#555a5e;
  --ink-soft:#9a9a9a;
  --rule:#d6d6d6;
  --chrome:#e4e4e4;
  --chrome-dark:#bdbdbd;
  --bar-green:#7ea93a;
  --bar-green-light:#a9cc5d;
  --cta-top:#2a9af3;
  --cta-bottom:#0a72e0;
}
*{margin:0;padding:0;box-sizing:border-box}
html,body{width:1200px;height:671px;overflow:hidden;background:var(--white);font-family:"Arimo",Arial,sans-serif}
.page{position:relative;width:1200px;height:671px}
.hero{position:absolute;left:0;top:0;width:1200px;height:437px;
  background:radial-gradient(ellipse 620px 360px at 600px 150px,var(--sky-light) 0%,var(--sky) 55%,var(--sky-deep) 100%)}
.header{position:absolute;left:0;top:0;width:1200px;height:90px;border-bottom:1px solid rgba(255,255,255,.35)}
.brand{position:absolute;left:170px;top:28px;color:var(--white);font-size:40px;font-weight:400;letter-spacing:1px;line-height:1}
.search{position:absolute;left:864px;top:18px;width:191px;height:23px;border:1px solid #35d0e8;background:rgba(20,130,180,.45)}
.search svg{position:absolute;right:7px;top:4px}
.nav{position:absolute;left:585px;top:63px;display:flex;color:var(--white);font-size:17.5px;line-height:20px}
.nav span{display:block}
.nav .sep{margin:0 20px}
.nav .active{position:relative}
.nav .active::after{content:"";position:absolute;left:-17px;right:-10px;top:24px;height:3px;background:var(--white)}
.nav .caret{font-size:9px;vertical-align:middle;margin-left:-26px;margin-right:18px}
.band{position:absolute;left:0;top:437px;width:1200px;height:94px;background:linear-gradient(#ffffff,#ececec);border-bottom:1px solid var(--rule)}
.browser{position:absolute;left:390px;top:195px;width:418px;height:296px;background:var(--chrome);border:1px solid var(--chrome-dark);border-radius:3px;overflow:hidden}
.browser-bar{height:32px;background:linear-gradient(#efefef,#d6d6d6);position:relative}
.nav-buttons{position:absolute;left:7px;top:7px;width:56px;height:18px;border:1px solid #a8a8a8;border-radius:3px;background:linear-gradient(#f2f2f2,#cfcfcf)}
.nav-buttons::after{content:"";position:absolute;left:27px;top:0;width:1px;height:16px;background:#a8a8a8}
.nav-buttons svg{position:absolute;top:4px}
.address{position:absolute;left:72px;top:7px;width:340px;height:18px;background:var(--white);border:1px solid #c3c3c3;border-radius:3px;font-size:8.5px;color:#777;padding:3px 0 0 7px}
.site-bar{height:26px;background:var(--sky);color:var(--white);font-size:14px;padding:6px 0 0 28px}
.poll-card{position:absolute;left:27px;top:74px;width:367px;height:222px;background:var(--white);box-shadow:0 0 2px rgba(0,0,0,.12)}
.poll-title{height:35px;border-bottom:1px solid #e4e4e4;padding:11px 0 0 19px;font-size:15px;color:var(--ink)}
.option{position:absolute;left:26px;width:314px}
.option-label{font-size:13px;color:var(--ink);display:flex;justify-content:space-between;padding-right:6px}
.option-label .votes{color:var(--ink-soft)}
.track{margin-top:3px;height:12px;border:1px solid #c8c8c8;background:linear-gradient(#fafafa,#e8e8e8);padding:1px}
.fill{height:8px;border:1px solid #5f8a22;background:linear-gradient(var(--bar-green-light),var(--bar-green))}
.vote-now{position:absolute;left:28px;top:180px;font-size:16px;color:var(--ink);display:flex;align-items:center;gap:10px}
.browser-foot{position:absolute;left:0;bottom:0;width:100%;height:7px;background:#d2d2d2;border-top:1px solid #bcbcbc}
.signup-tab{position:absolute;left:1160px;top:217px;width:40px;height:157px;border:3px solid var(--white);border-right:none;background:linear-gradient(90deg,#6ccdf2,#2fa6dc)}
.signup-tab .label{position:absolute;left:50%;top:58px;transform:translate(-50%,-50%) rotate(-90deg);color:var(--white);font-weight:700;font-size:21px;white-space:nowrap;letter-spacing:1px}
.signup-tab svg{position:absolute;left:8px;top:119px}
.cta{position:absolute;left:513px;top:509px;width:175px;height:46px;border-radius:5px;background:linear-gradient(var(--cta-top),var(--cta-bottom));border:1px solid #0b68c8;color:var(--white);font-weight:700;font-size:20px;text-align:center;line-height:44px}
.tagline{position:absolute;left:0;top:568px;width:1200px;text-align:center;font-size:19.5px;color:var(--ink)}
.footer-rule{position:absolute;left:0;top:607px;width:1200px;height:1px;background:var(--rule)}
.copyright{position:absolute;left:0;top:628px;width:1200px;text-align:center;font-size:12.5px;color:var(--ink)}
</style>
</head>
<body>
<div class="page">
  <div class="hero" role="img" aria-label="Light rays radiating from the centre of a bright blue background"></div>

  <header class="header">
    <div class="brand">VOTIQO</div>
    <div class="search">
      <svg width="14" height="14" viewBox="0 0 14 14"><circle cx="6" cy="6" r="4.5" fill="none" stroke="#cdeef9" stroke-width="1.4"/><line x1="9.3" y1="9.3" x2="13" y2="13" stroke="#cdeef9" stroke-width="1.6"/></svg>
    </div>
    <nav class="nav">
      <span>My profile</span><span class="sep">|</span>
      <span class="active">Post a new poll</span><span class="sep">|</span>
      <span>View friends</span><span class="sep">|</span>
      <span>Poll topics</span><span class="caret">▼</span>
    </nav>
  </header>

  <div class="band"></div>

  <div class="browser">
    <div class="browser-bar">
      <div class="nav-buttons">
        <svg style="left:9px" width="9" height="9" viewBox="0 0 9 9"><polygon points="8,0 8,9 0,4.5" fill="#777"/></svg>
        <svg style="left:37px" width="9" height="9" viewBox="0 0 9 9"><polygon points="0,0 0,9 8,4.5" fill="#777"/></svg>
      </div>
      <div class="address">www.votiqo.com</div>
    </div>
    <div class="site-bar">VOTIQO</div>

    <div class="poll-card">
      <div class="poll-title">Votiqo&nbsp; polling demo</div>
      <div class="option" style="top:50px">
        <div class="option-label"><span>Awesome</span><span class="votes">150 votes</span></div>
        <div class="track"><div class="fill" style="width:284px"></div></div>
      </div>
      <div class="option" style="top:89px">
        <div class="option-label"><span>Good</span><span class="votes">95 votes</span></div>
        <div class="track"><div class="fill" style="width:171px"></div></div>
      </div>
      <div class="option" style="top:127px">
        <div class="option-label"><span>ok</span><span class="votes">50 votes</span></div>
        <div class="track"><div class="fill" style="width:74px"></div></div>
      </div>
      <div class="vote-now">Vote now
        <svg width="20" height="14" viewBox="0 0 20 14"><polygon points="0,0 10,7 0,14" fill="#9aa0a4"/><polygon points="9,0 19,7 9,14" fill="#9aa0a4"/></svg>
      </div>
    </div>
    <div class="browser-foot"></div>
  </div>

  <a class="signup-tab" aria-label="Sign up">
    <span class="label">SIGN UP</span>
    <svg width="22" height="22" viewBox="0 0 22 22"><circle cx="14" cy="7" r="6" fill="#fff"/><path d="M2 22 Q3 12 10 12 L18 12 Q22 14 22 22 Z" fill="#fff"/></svg>
  </a>

  <div class="cta">Sign up now</div>
  <p class="tagline">Lorem Ipsum is simply dummy text of the printing and typesetting industry.</p>
  <div class="footer-rule"></div>
  <p class="copyright">Copyright © 2012 Votiqo. Use of this website constitutes acceptance of our User Agreement and Privacy Policy</p>
</div>
</body>
</html>
```